Technology Solutions Provider

Let’s design a business card that will be as simple and bold at the same time. Name, email address, website & phone number.

Target Market(s)

Small to Medium Size Business

Industry/Entity Type

It Professional

Contact Information for Business Card

Name, email, website, phone numbers

Font styles to use
Sans Serif

Colors
ec1f27
f04a50
dddddd
919191
000000
ffffff

Requirements
Must have
• Clean simple look using my existing logo. I just need to the basic contact information on this card.
Nice to have
• Im considering the square size card versus the standard size business card.
Should not have
• No Mailing Address, no list of services.

```html
<!DOCTYPE html>
<html lang="en">
<head>
<meta charset="utf-8">
<title>Corelink Networks – Business Card</title>
<link rel="stylesheet" href="https://fonts.googleapis.com/css2?family=Montserrat:wght@400;500&display=swap">
<style>
  :root {
    --red: #ec1f27;
    --red-soft: #f04a50;
    --rule: #919191;
    --light: #dddddd;
    --ink: #000000;
    --paper: #ffffff;
    --backdrop: #2b2b2b;
  }
  * { margin: 0; padding: 0; box-sizing: border-box; }
  html, body { width: 1200px; height: 880px; overflow: hidden; }
  body {
    background: var(--backdrop);
    display: flex;
    align-items: center;
    justify-content: center;
    gap: 48px;
    font-family: "Montserrat", sans-serif;
  }
  .card {
    width: 540px;
    height: 310px;
    background: var(--paper);
    border-radius: 18px;
    box-shadow: 0 16px 40px rgba(0,0,0,.45);
    display: flex;
    align-items: center;
    justify-content: center;
  }
  /* Front */
  .company-name {
    font-size: 34px;
    font-weight: 500;
    color: var(--ink);
    letter-spacing: .5px;
    line-height: 1;
  }
  /* Back */
  .identity { text-align: right; padding-right: 18px; }
  .person-name { font-size: 24px; font-weight: 500; color: var(--ink); line-height: 1.1; }
  .person-role { font-size: 16px; color: var(--red); }
  .divider { width: 1px; height: 64px; background: var(--rule); }
  .contacts { list-style: none; padding-left: 18px; }
  .contact {
    display: flex; align-items: center; gap: 8px;
    font-size: 14px; color: var(--ink); line-height: 1.55;
  }
  .contact svg { width: 16px; height: 16px; flex: none; }
</style>
</head>
<body>
  <section class="card card-front">
    <p class="company-name">corelink networks</p>
  </section>

  <section class="card card-back">
    <div class="identity">
      <p class="person-name">Daniel Reyes</p>
      <p class="person-role">Founder</p>
    </div>
    <span class="divider"></span>
    <ul class="contacts">
      <li class="contact">
        <svg viewBox="0 0 16 16" aria-hidden="true"><circle cx="8" cy="8" r="7" fill="none" stroke="#ec1f27" stroke-width="1.3"/><path d="M5 5.5c0 3 2.5 5.5 5.5 5.5l.7-1.4-1.5-.8-.7.7c-1-.5-1.8-1.3-2.3-2.3l.7-.7-.8-1.5z" fill="#ec1f27"/></svg>
        (555) 214-3098
      </li>
      <li class="contact">
        <svg viewBox="0 0 16 16" aria-hidden="true"><circle cx="8" cy="8" r="7" fill="none" stroke="#ec1f27" stroke-width="1.3"/><rect x="4.5" y="5.5" width="7" height="5" fill="none" stroke="#ec1f27" stroke-width="1"/><path d="M4.5 5.5L8 8.3l3.5-2.8" fill="none" stroke="#ec1f27" stroke-width="1"/></svg>
        hello@corelinkit.com
      </li>
      <li class="contact">
        <svg viewBox="0 0 16 16" aria-hidden="true"><circle cx="8" cy="8" r="7" fill="none" stroke="#ec1f27" stroke-width="1.3"/><circle cx="8" cy="8" r="3.6" fill="none" stroke="#ec1f27" stroke-width="1"/><path d="M4.4 8h7.2M8 4.4c-1.5 2-1.5 5.2 0 7.2M8 4.4c1.5 2 1.5 5.2 0 7.2" fill="none" stroke="#ec1f27" stroke-width=".8"/></svg>
        www.corelinkit.com
      </li>
    </ul>
  </section>
</body>
</html>
```